MEDITERRANEAN Cafe Website needed

We are a MEDITERRANEAN Café serving Coffee, breakfast, Pizza, Pasta, Sandwiches etc.

We need a home page, menu & venue, Reservations & Events, Delivery
Connect (Social media / Feedback / Contact us),Join our team
Updates

Can we keep the designs in Mediterranean colours, look, and feel pleasethanks Added Saturday, December 10, 2016

Project Deadline Extended Reason: I have guarantied the payment and upgraded the project. I would like this would to give more time for new designs to come in and a couple of potential designs to show more. Added Sunday, December 11, 2016

Industry/Entity Type

Cafe

Coding

Coded - Design and coding required

Number of Pages Required

5+ page

Requirements
Must have
• MEDITERRANEAN feel, colours, style etc.
• http://www.quillandfen (DOT) co (DOT) uk
Nice to have

```html
<!DOCTYPE html>
<html lang="en">
<head>
<meta charset="utf-8">
<title>Solana Cafe – Wraps &amp; Grill</title>
<link href="https://fonts.googleapis.com/css2?family=Noto+Serif:wght@400;700&family=Open+Sans:wght@400;600;700&family=Pinyon+Script&display=swap" rel="stylesheet">
<style>
:root{
  --red:#ee3b3b;
  --ink:#3b3d42;
  --ink-dark:#2f3135;
  --paper:#e6d1ab;
  --paper-deep:#d8bd92;
  --text:#5b5247;
  --white:#ffffff;
  --tan:#b7a78d;
}
*{box-sizing:border-box;margin:0;padding:0}
html,body{width:1200px;height:3025px;overflow:hidden}
body{font-family:"Open Sans",Arial,sans-serif;color:var(--text);background:var(--paper);position:relative}

/* hero */
.hero{position:absolute;left:0;top:0;width:1200px;height:630px;
  background:
    radial-gradient(ellipse 120px 90px at 150px 270px,rgba(196,52,38,.75),transparent 70%),
    radial-gradient(ellipse 520px 200px at 620px 260px,rgba(238,230,218,.9),transparent 70%),
    radial-gradient(ellipse 260px 120px at 820px 430px,rgba(84,120,50,.55),transparent 70%),
    linear-gradient(180deg,#5a3e2b 0%,#7b5a40 45%,#4a3122 100%)}
.hero::after{content:"";position:absolute;inset:0;background:rgba(20,12,8,.25)}
.nav,.hero h1,.hero .btn,.arrow{z-index:1}
.nav{position:absolute;left:100px;top:90px;width:1000px;height:56px}
.nav svg{position:absolute;left:0;top:0}
.nav a{position:absolute;top:15px;color:var(--white);font-size:14px;text-decoration:none;font-family:"Noto Serif",Georgia,serif;padding:4px 12px;border-radius:3px}
.nav a.active{background:var(--red)}
.brand-badge{position:absolute;display:flex;align-items:center;justify-content:center;border-radius:50%;background:var(--red);color:var(--white);font-family:"Noto Serif",Georgia,serif;font-weight:700}
.nav .brand-badge{left:415px;top:-42px;width:140px;height:140px;font-size:30px;border:4px solid var(--ink)}
.hero h1{position:absolute;left:0;width:1200px;top:316px;text-align:center;color:var(--white);font-family:"Noto Serif",Georgia,serif;font-size:60px;font-weight:700}
.btn{display:inline-block;background:var(--red);color:var(--white);font-family:"Noto Serif",Georgia,serif;font-weight:700;font-size:13px;padding:7px 18px;border-radius:16px;text-transform:uppercase;letter-spacing:.3px}
.hero .btn{position:absolute;left:540px;top:406px;padding:9px 20px;border:2px solid #f7a0a0}
.arrow{position:absolute;top:352px;width:34px;height:34px;border-radius:50%;background:var(--ink-dark);display:flex;align-items:center;justify-content:center}

/* paper */
.paper{position:absolute;left:0;top:630px;width:1200px;height:2002px;
  background:radial-gradient(ellipse at 50% 40%,#efdfbf 0%,var(--paper) 55%,var(--paper-deep) 100%)}

.offer{position:absolute;top:66px;width:320px;text-align:center}
.offer .icon{margin:0 auto;width:170px;height:130px;border-radius:50%;background:var(--red);display:flex;align-items:center;justify-content:center}
.offer h2{font-family:"Noto Serif",Georgia,serif;font-size:32px;color:var(--ink);margin-top:30px;line-height:1}
.offer h3{font-family:"Noto Serif",Georgia,serif;font-size:18px;color:var(--ink);margin-top:4px;font-weight:700;text-transform:uppercase}
.offer p{font-family:"Noto Serif",Georgia,serif;font-size:11.5px;line-height:19px;margin:10px 0 16px}
.offer .icon.brand-badge{position:static;font-size:30px}

.events{position:absolute;left:99px;top:477px;width:1002px;height:410px}
.events .panel{position:absolute;left:0;top:0;width:322px;height:410px;background:var(--red);padding:140px 0 0 36px;color:var(--white)}
.events .panel h2{font-family:"Noto Serif",Georgia,serif;font-size:32px;font-weight:700}
.events .panel p{font-family:"Noto Serif",Georgia,serif;font-weight:700;font-size:13px;line-height:22px;margin:12px 0 24px;text-transform:uppercase}
.events .outline{border:1px solid var(--white);color:var(--white);font-family:"Noto Serif",Georgia,serif;font-size:13px;font-weight:700;padding:6px 14px;display:inline-block}
.events .photo{position:absolute;left:322px;top:0;width:680px;height:410px;
  background:
    radial-gradient(ellipse 170px 200px at 190px 180px,rgba(240,232,220,.95),transparent 70%),
    radial-gradient(ellipse 220px 140px at 500px 150px,rgba(236,178,52,.95),transparent 70%),
    radial-gradient(ellipse 380px 110px at 360px 340px,rgba(150,100,60,.9),transparent 70%),
    linear-gradient(180deg,#7d8088 0%,#8a8c92 100%)}
.events .notch{position:absolute;left:320px;top:140px}

.menu-head{position:absolute;left:0;width:1200px;top:960px;text-align:center}
.ribbon{display:inline-block;position:relative;width:262px;height:52px}
.ribbon span{position:absolute;inset:0;display:flex;align-items:center;justify-content:center;color:var(--white);font-family:"Noto Serif",Georgia,serif;font-weight:700;font-size:28px}
.menu-head p{font-size:14px;margin-top:16px}

.cards{position:absolute;left:99px;top:1088px;display:flex;gap:22px}
.card{width:234px;height:307px;background:var(--white);position:relative;text-align:center}
.card .photo{height:190px}
.card .badge{position:absolute;left:97px;top:171px;width:40px;height:40px;border-radius:50%;background:var(--tan);border:3px solid var(--white);display:flex;align-items:center;justify-content:center}
.card h4{font-family:"Noto Serif",Georgia,serif;font-weight:400;font-size:15px;color:var(--ink);margin-top:30px;text-transform:uppercase}
.card p{font-size:11px;line-height:19px;margin:6px 10px 0}

.story-photos{position:absolute;left:99px;top:1500px;display:grid;grid-template-columns:258px 260px;grid-gap:10px}
.story-photos div{height:180px}
.story{position:absolute;left:678px;top:1512px;width:426px}
.story .script{font-family:"Pinyon Script",cursive;font-size:40px;color:var(--ink);line-height:1}
.story h2{font-family:"Noto Serif",Georgia,serif;font-size:44px;color:var(--red);line-height:1.05;font-weight:700}
.story p{font-size:11px;line-height:23.5px;margin-top:14px}
.story .btn{border-radius:4px;margin-top:16px;font-weight:400;font-size:14px;text-transform:none;padding:6px 13px}

/* newsletter */
.newsletter{position:absolute;left:100px;top:2588px;width:1000px;height:90px;z-index:2}
.newsletter svg{position:absolute;left:0;top:0}
.newsletter .msg{position:absolute;left:138px;top:26px;color:var(--white);font-size:15px;line-height:19px;text-transform:uppercase}
.newsletter .field{position:absolute;left:420px;top:25px;width:375px;height:40px;background:var(--white);border-radius:20px 0 0 20px;font-size:13px;color:#777;padding:11px 20px}
.newsletter .subscribe{position:absolute;left:795px;top:25px;width:126px;height:40px;background:var(--ink-dark);border-radius:0 20px 20px 0;color:var(--white);font-size:13px;display:flex;align-items:center;justify-content:center;font-weight:600}

/* footer */
.footer{position:absolute;left:0;top:2632px;width:1200px;height:393px;background:var(--ink);color:var(--white)}
.footer h5{font-family:"Noto Serif",Georgia,serif;font-weight:400;font-size:16px;text-transform:uppercase;letter-spacing:.3px}
.footer .brand-badge{left:100px;top:138px;width:160px;height:130px;font-size:30px}
.contact{position:absolute;left:308px;top:102px;width:250px}
.contact li{list-style:none;display:flex;gap:16px;font-size:12px;line-height:21px;margin-top:18px}
.contact svg{flex:none;margin-top:3px}
.location{position:absolute;left:584px;top:102px}
.map{margin-top:16px;width:338px;height:156px;background:linear-gradient(135deg,#dadada,#c4c4c4);border:3px solid #e9e9e9}
.links{position:absolute;left:990px;top:102px}
.links li{list-style:none;font-size:12px;margin-top:6px;line-height:18px}
.links li::before{content:"";display:inline-block;border-left:5px solid var(--white);border-top:4px solid transparent;border-bottom:4px solid transparent;margin-right:12px}
.links ul{margin-top:20px}
.copyright{position:absolute;left:0;top:352px;width:1200px;border-top:1px solid #4c4e53;padding-top:12px;text-align:center;font-size:11px;color:#ddd}
</style>
</head>
<body>

<header class="hero" role="img" aria-label="Photo of a grilled chicken wrap with salad and tomatoes on a wooden board">
  <nav class="nav">
    <svg width="1000" height="56" viewBox="0 0 1000 56"><polygon points="16,2 984,2 998,28 984,54 16,54 2,28" fill="#4a4c52" stroke="#cfd0d2" stroke-width="3"/></svg>
    <a class="active" style="left:28px">Home</a>
    <a style="left:108px">About Us</a>
    <a style="left:207px">Our Menu</a>
    <a style="left:313px">Events</a>
    <div class="brand-badge">Solana</div>
    <a style="left:582px">Our Story</a>
    <a style="left:682px">Careers</a>
    <a style="left:770px">Location</a>
    <a style="left:870px">Contact</a>
  </nav>
  <div class="arrow" style="left:46px"><svg width="12" height="12" viewBox="0 0 12 12"><path d="M8 1 3 6l5 5" stroke="#fff" stroke-width="2.4" fill="none"/></svg></div>
  <div class="arrow" style="left:1118px"><svg width="12" height="12" viewBox="0 0 12 12"><path d="M4 1l5 5-5 5" stroke="#fff" stroke-width="2.4" fill="none"/></svg></div>
  <h1>Wraps &amp; Grill Shop</h1>
  <span class="btn">View Menu ›</span>
</header>

<main class="paper">
  <section class="offer" style="left:82px">
    <div class="icon"><svg width="70" height="70" viewBox="0 0 70 70" fill="none" stroke="#fff" stroke-width="4"><circle cx="35" cy="38" r="24"/><circle cx="35" cy="38" r="9"/><path d="M20 12l10 8M50 12l-10 8"/></svg></div>
    <h2>BREAKFAST</h2>
    <h3>From £4.75</h3>
    <p>Sed ut perspiciatis unde omnis iste natus error sit voluptatem accusantium doloremque laudantium, totam rem aperiam, eaque ipsa quae</p>
    <span class="btn">View Menu ›</span>
  </section>
  <section class="offer" style="left:437px">
    <div class="icon"><svg width="90" height="70" viewBox="0 0 90 70" fill="none" stroke="#fff" stroke-width="4"><circle cx="45" cy="35" r="20"/><path d="M14 10v50M9 10v16q5 6 10 0V10M76 10q-8 12 0 28v22"/></svg></div>
    <h2>LUNCH</h2>
    <h3>From £6.95</h3>
    <p>Sed ut perspiciatis unde omnis iste natus error sit voluptatem accusantium doloremque laudantium, totam rem aperiam, eaque ipsa quae</p>
    <span class="btn">View Menu ›</span>
  </section>
  <section class="offer" style="left:796px">
    <div class="icon brand-badge">Solana</div>
    <h2>MAIN MENU</h2>
    <h3 style="font-size:15px">Enjoy the taste of Italy</h3>
    <p>Sed ut perspiciatis unde omnis iste natus error sit voluptatem accusantium doloremque laudantium, totam rem aperiam, eaque ipsa quae</p>
    <span class="btn">View Menu ›</span>
  </section>

  <section class="events">
    <div class="photo" role="img" aria-label="Photo of a sliced chicken wrap with fries on a wooden board"></div>
    <div class="panel">
      <h2>OUR EVENTS</h2>
      <p>All of your Solana Café favorites<br>are available, just right, easily<br>and affordable.</p>
      <span class="outline">VIEW MENU ›</span>
    </div>
    <svg class="notch" width="22" height="44" viewBox="0 0 22 44"><polygon points="0,0 22,22 0,44" fill="#ee3b3b"/></svg>
  </section>

  <section class="menu-head">
    <div class="ribbon">
      <svg width="262" height="52" viewBox="0 0 262 52"><polygon points="14,3 248,3 259,26 248,49 14,49 3,26" fill="#4a4c52" stroke="#fff" stroke-width="3"/></svg>
      <span>OUR MENU</span>
    </div>
    <p>Choice of Sides includes Fries, Mashed or Baked Potatoes, Butter Rice</p>
  </section>

  <section class="cards">
    <article class="card">
      <div class="photo" role="img" aria-label="Photo of a doner wrap with orange slices" style="background:radial-gradient(ellipse 110px 70px at 110px 80px,#8a3f25,transparent 75%),radial-gradient(ellipse 90px 50px at 60px 175px,#f0a020,transparent 75%),linear-gradient(160deg,#e8dcc8,#b98258)"></div>
      <div class="badge"><svg width="16" height="16" viewBox="0 0 16 16"><path d="M2 2l12 12M14 2 2 14" stroke="#fff" stroke-width="2"/></svg></div>
      <h4>Breakfast</h4>
      <p>Lorem ipsum dolor sit amet, consetur adipiscing elit, sed do eiusmod</p>
    </article>
    <article class="card">
      <div class="photo" role="img" aria-label="Photo of grilled meat skewers with lemon" style="background:radial-gradient(ellipse 100px 60px at 120px 120px,#b8642e,transparent 75%),radial-gradient(ellipse 40px 40px at 200px 50px,#f0d050,transparent 75%),linear-gradient(135deg,#4f6b2e,#8a5a30 60%,#d9c79a)"></div>
      <div class="badge"><svg width="16" height="16" viewBox="0 0 16 16"><path d="M2 2l12 12M14 2 2 14" stroke="#fff" stroke-width="2"/></svg></div>
      <h4>Fish&amp;Meat</h4>
      <p>Lorem ipsum dolor sit amet, consetur adipiscing elit, sed do eiusmod</p>
    </article>
    <article class="card">
      <div class="photo" role="img" aria-label="Photo of grilled chicken wings with lemon" style="background:radial-gradient(ellipse 100px 70px at 110px 110px,#b5542a,transparent 75%),radial-gradient(ellipse 40px 30px at 120px 90px,#f2d040,transparent 75%),linear-gradient(160deg,#7d8a99,#e8e4dc 70%)"></div>
      <div class="badge"><svg width="16" height="16" viewBox="0 0 16 16"><path d="M2 2l12 12M14 2 2 14" stroke="#fff" stroke-width="2"/></svg></div>
      <h4>Wraps &amp; Grill</h4>
      <p>Lorem ipsum dolor sit amet, consetur adipiscing elit, sed do eiusmod</p>
    </article>
    <article class="card">
      <div class="photo" role="img" aria-label="Photo of a mushroom pizza" style="background:radial-gradient(ellipse 130px 110px at 120px 100px,#ead9b0,#c99a5a 60%,transparent 80%),linear-gradient(135deg,#8a5a30,#5a3a22)"></div>
      <div class="badge"><svg width="16" height="16" viewBox="0 0 16 16"><path d="M2 2l12 12M14 2 2 14" stroke="#fff" stroke-width="2"/></svg></div>
      <h4>Pizza</h4>
      <p>Lorem ipsum dolor sit amet, consetur adipiscing elit, sed do eiusmod</p>
    </article>
  </section>

  <section class="story-photos">
    <div role="img" aria-label="Photo of grilled halloumi with olives and tomatoes" style="background:radial-gradient(ellipse 90px 70px at 80px 110px,#e5b870,transparent 75%),radial-gradient(ellipse 60px 40px at 200px 60px,#3a2a2a,transparent 75%),linear-gradient(135deg,#f2ece2,#c8503a 70%)"></div>
    <div role="img" aria-label="Photo of chicken wings with dip" style="background:radial-gradient(ellipse 100px 70px at 140px 100px,#b6682c,transparent 75%),radial-gradient(ellipse 40px 30px at 40px 40px,#f2efe6,transparent 75%),linear-gradient(135deg,#4a3a30,#7a5a40)"></div>
    <div role="img" aria-label="Photo of a burger with fries" style="background:radial-gradient(ellipse 110px 60px at 110px 80px,#6a3a22,transparent 75%),radial-gradient(ellipse 130px 40px at 120px 160px,#f0c050,transparent 75%),linear-gradient(180deg,#3a2a22,#7a4a2a)"></div>
    <div role="img" aria-label="Photo of a burger and fries on a plate" style="background:radial-gradient(ellipse 120px 70px at 130px 110px,#f0d7a0,transparent 75%),radial-gradient(ellipse 70px 40px at 120px 50px,#8a4a2a,transparent 75%),linear-gradient(135deg,#b84a3a,#d88a5a)"></div>
  </section>

  <section class="story">
    <div class="script">Discover</div>
    <h2>OUR STORY</h2>
    <p>An early morning walk to the bakery around the corner is a way of life in the Mediterranean.&nbsp; Nothing beats the first batch of bread from the oven to start your day. Solana Cafe started with a simple idea," we wanted people to experience that taste all the time". So we combined a variety of best ingredients and delicacies to make you that healthy stuffed all fresh Pita to enjoy the way you like and whenever you got the urge to do so.</p>
    <p>As time went by we opened our hearts and ears to our customers and added a range of fresh and delicious products to our menu.</p>
    <span class="btn">Read More</span>
  </section>
</main>

<section class="newsletter">
  <svg width="1000" height="90" viewBox="0 0 1000 90"><polygon points="22,0 978,0 1000,45 978,90 22,90 0,45" fill="#ee3b3b"/><polygon points="30,8 970,8 989,45 970,82 30,82 11,45" fill="none" stroke="#fff" stroke-width="2"/>
    <g transform="translate(78,25)" fill="none" stroke="#fff" stroke-width="2.5"><rect x="0" y="6" width="40" height="28"/><path d="M0 6l20 16 20-16"/></g></svg>
  <div class="msg">Make sure to sign up for our<br>newsletter to stay informed!</div>
  <div class="field">Enter your E - mail</div>
  <div class="subscribe">SUBSCRIBE</div>
</section>

<footer class="footer">
  <div class="brand-badge">Solana</div>
  <div class="contact">
    <h5>Contact Us</h5>
    <ul>
      <li><svg width="14" height="18" viewBox="0 0 14 18" fill="none" stroke="#fff" stroke-width="1.6"><path d="M7 17S1 10 1 6.5a6 6 0 0 1 12 0C13 10 7 17 7 17z"/><circle cx="7" cy="6.5" r="2"/></svg><span>Solana Cafe, Level 2|14 Harbour<br>Lane|Westbrook Vale<br>VIC 3999</span></li>
      <li><svg width="16" height="16" viewBox="0 0 16 16" fill="none" stroke="#fff" stroke-width="1.6"><path d="M3 1l3 3-2 2q2 4 6 6l2-2 3 3-2 2Q6 14 1 3z"/></svg><span>Phone : 1300 000 482</span></li>
      <li><svg width="16" height="14" viewBox="0 0 16 14" fill="none" stroke="#fff" stroke-width="1.6"><rect x="1" y="2" width="14" height="10"/><path d="M1 2l7 6 7-6"/></svg><span>hello@solanacafe.example</span></li>
    </ul>
  </div>
  <div class="location">
    <h5>Our Location</h5>
    <div class="map" role="img" aria-label="Street map showing the cafe location"></div>
  </div>
  <div class="links">
    <h5>Quick Links</h5>
    <ul>
      <li>Home</li><li>About Us</li><li>Our Menu</li><li>Our Story</li><li>Events</li><li>Location</li><li>Contact Us</li>
    </ul>
  </div>
  <div class="copyright">Copyright 2016 | All Rights Reserved –Solana Cafe</div>
</footer>

</body>
</html>
```